logo/ product label

We handcraft and infuse organically grown herbs to create body products (lotions, massage oils, face creams and healing salves) and tinctures for resale and use in our massage therapy office on the harbor of Camden, Maine. Our new venture is called "Larkspur Cove Company", and we like the idea of a vintage apothecary looking label and a logo that works well incorporating the sea, and our herbal healthy and pure product line. We have a tourist, yacht ...and local clientele.

Target Market(s)

clients wanting healthy products for their skin ,
tourists wanting to "bring it home" from their vacation

Industry/Entity Type

Product

Font styles to use
Decorative

Colors
fde08a
cadf82
faf289
acd036
33b7a4
fff3d0
fbc994
cfeae6

Requirements
Must have
• simple, understandable camden maine ocean vacation with handcrafted herbal products to bring home
• understated
Nice to have
• elegant and subtle /modern or vintage logo, to be shown on cobalt blue glass or aluminum tins
Should not have
• flashy, airbrushy,

```html
<!DOCTYPE html>
<html lang="en">
<head>
<meta charset="utf-8">
<title>Larkspur Cove Company – Product Labels</title>
<link rel="stylesheet" href="https://fonts.googleapis.com/css2?family=IM+Fell+English+SC&family=Pinyon+Script&family=Cormorant+Garamond:wght@500&display=swap">
<style>
  :root {
    --paper: #e7e2d7;
    --paper-edge: #dcd6c8;
    --ink: #141414;
    --glow-peach: #fbc994;
    --glow-green: #b7e3a6;
    --glow-sea: #9fd6e0;
    --sketch-grey: #8d8a86;
    --page: #ffffff;
  }
  html, body {
    margin: 0;
    padding: 0;
    width: 1200px;
    height: 591px;
    overflow: hidden;
    background: var(--page);
  }
  .label-sheet { display: block; width: 1200px; height: 591px; }
  .label-outer { fill: var(--paper); stroke: var(--paper-edge); stroke-width: 2; }
  .label-frame-bold { fill: none; stroke: var(--ink); stroke-width: 9; stroke-linejoin: miter; }
  .label-frame-fine { fill: none; stroke: var(--ink); stroke-width: 3; stroke-linejoin: miter; }
  .state-mark { font-family: "Cormorant Garamond", serif; font-size: 15px; letter-spacing: 2px; fill: var(--ink); }
  .brand-name { font-family: "IM Fell English SC", serif; font-size: 40px; letter-spacing: 3px; fill: var(--ink); }
  .product-line { font-family: "IM Fell English SC", serif; font-size: 30px; letter-spacing: 5px; fill: var(--ink); }
  .product-line--small { font-size: 20px; letter-spacing: 3px; }
  .product-name { font-family: "Pinyon Script", cursive; font-size: 66px; fill: var(--ink); }
  .established { font-family: "Cormorant Garamond", serif; font-size: 16px; fill: var(--ink); }
  .rule { stroke: var(--ink); stroke-width: 1.5; }
  .rule-dot { fill: var(--ink); }
  .ornament-slot { fill: url(#ornamentTone); }
  .sketch-slot { fill: url(#sketchTone); }
  .sprig-slot { fill: url(#sprigTone); }
</style>
</head>
<body>
<svg class="label-sheet" viewBox="0 0 1200 591" xmlns="http://www.w3.org/2000/svg">
  <defs>
    <radialGradient id="glowPeach" cx="0.5" cy="0.5" r="0.5">
      <stop offset="0" stop-color="var(--glow-peach)" stop-opacity="0.95"/>
      <stop offset="1" stop-color="var(--glow-peach)" stop-opacity="0"/>
    </radialGradient>
    <radialGradient id="glowGreen" cx="0.5" cy="0.5" r="0.5">
      <stop offset="0" stop-color="var(--glow-green)" stop-opacity="0.9"/>
      <stop offset="1" stop-color="var(--glow-green)" stop-opacity="0"/>
    </radialGradient>
    <radialGradient id="glowSea" cx="0.5" cy="0.5" r="0.5">
      <stop offset="0" stop-color="var(--glow-sea)" stop-opacity="0.9"/>
      <stop offset="1" stop-color="var(--glow-sea)" stop-opacity="0"/>
    </radialGradient>
    <linearGradient id="ornamentTone" x1="0" x2="1">
      <stop offset="0" stop-color="#6d6b68" stop-opacity="0.35"/>
      <stop offset="0.5" stop-color="#2a2a2a" stop-opacity="0.6"/>
      <stop offset="1" stop-color="#6d6b68" stop-opacity="0.35"/>
    </linearGradient>
    <linearGradient id="sketchTone" x1="0" y1="0" x2="0" y2="1">
      <stop offset="0" stop-color="#3a3a3a" stop-opacity="0.55"/>
      <stop offset="1" stop-color="var(--sketch-grey)" stop-opacity="0.3"/>
    </linearGradient>
    <linearGradient id="sprigTone" x1="0" x2="1">
      <stop offset="0" stop-color="#5c5a6a" stop-opacity="0.2"/>
      <stop offset="1" stop-color="#5c5a6a" stop-opacity="0.5"/>
    </linearGradient>
    <clipPath id="innerShape">
      <polygon points="174,38 416,38 552,174 552,417 416,553 174,553 38,417 38,174"/>
    </clipPath>
    <path id="arcWide" d="M 95 405 A 230 230 0 0 1 495 405"/>
    <path id="arcNarrow" d="M 163 470 A 160 160 0 0 1 428 470"/>
  </defs>

  <!-- Label: Organic Infusions -->
  <g class="label label--infusions">
    <polygon class="label-outer" points="150,3 440,3 587,150 587,441 440,588 150,588 3,441 3,150"/>
    <g clip-path="url(#innerShape)">
      <ellipse cx="300" cy="330" rx="190" ry="170" fill="url(#glowPeach)"/>
      <ellipse cx="190" cy="490" rx="200" ry="130" fill="url(#glowGreen)"/>
      <ellipse cx="460" cy="480" rx="190" ry="140" fill="url(#glowSea)"/>
    </g>
    <polygon class="label-frame-bold" points="160,22 430,22 568,160 568,431 430,569 160,569 22,431 22,160"/>
    <polygon class="label-frame-fine" points="174,38 416,38 552,174 552,417 416,553 174,553 38,417 38,174"/>

    <text class="state-mark" x="295" y="78" text-anchor="middle">ME</text>
    <rect class="ornament-slot" x="170" y="88" width="250" height="14" rx="4" role="img" aria-label="Vintage scroll flourish"/>

    <text class="brand-name" x="295" y="158" text-anchor="middle">Larkspur Cove</text>
    <text class="brand-name" x="295" y="200" text-anchor="middle">Company</text>

    <line class="rule" x1="92" y1="228" x2="272" y2="228"/>
    <line class="rule" x1="318" y1="228" x2="498" y2="228"/>
    <circle class="rule-dot" cx="92" cy="228" r="2.5"/>
    <circle class="rule-dot" cx="498" cy="228" r="2.5"/>
    <rect class="ornament-slot" x="274" y="219" width="42" height="18" rx="3" role="img" aria-label="Small engraved centre ornament"/>

    <text class="product-line">
      <textPath href="#arcWide" startOffset="27%" text-anchor="middle">Organic</textPath>
    </text>
    <text class="product-line">
      <textPath href="#arcWide" startOffset="74%" text-anchor="middle">Infusions</textPath>
    </text>

    <rect class="sprig-slot" x="120" y="420" width="110" height="42" rx="18" role="img" aria-label="Sketched herb sprig"/>
    <rect class="sprig-slot" x="375" y="420" width="110" height="42" rx="18" transform="rotate(-12 430 441)" role="img" aria-label="Sketched herb sprig"/>
    <rect class="sketch-slot" x="255" y="315" width="80" height="205" rx="4" role="img" aria-label="Pen sketch of a coastal lighthouse on a rocky shore"/>

    <text class="established" x="295" y="540" text-anchor="middle">Est. 2014</text>
  </g>

  <!-- Label: Massage Oil -->
  <g class="label label--massage-oil" transform="translate(612 0)">
    <polygon class="label-outer" points="150,3 440,3 587,150 587,441 440,588 150,588 3,441 3,150"/>
    <g clip-path="url(#innerShape)">
      <ellipse cx="300" cy="330" rx="180" ry="130" fill="url(#glowPeach)"/>
      <ellipse cx="180" cy="500" rx="200" ry="130" fill="url(#glowGreen)"/>
      <ellipse cx="450" cy="490" rx="190" ry="140" fill="url(#glowSea)"/>
    </g>
    <polygon class="label-frame-bold" points="160,22 430,22 568,160 568,431 430,569 160,569 22,431 22,160"/>
    <polygon class="label-frame-fine" points="174,38 416,38 552,174 552,417 416,553 174,553 38,417 38,174"/>

    <text class="state-mark" x="295" y="80" text-anchor="middle">ME</text>
    <rect class="ornament-slot" x="170" y="90" width="250" height="14" rx="4" role="img" aria-label="Vintage scroll flourish"/>

    <text class="brand-name" x="295" y="162" text-anchor="middle">Larkspur Cove</text>
    <text class="brand-name" x="295" y="204" text-anchor="middle">Company</text>

    <line class="rule" x1="92" y1="232" x2="272" y2="232"/>
    <line class="rule" x1="318" y1="232" x2="498" y2="232"/>
    <circle class="rule-dot" cx="92" cy="232" r="2.5"/>
    <circle class="rule-dot" cx="498" cy="232" r="2.5"/>
    <rect class="ornament-slot" x="274" y="223" width="42" height="18" rx="3" role="img" aria-label="Small engraved centre ornament"/>

    <text class="product-name" x="295" y="312" text-anchor="middle">Massage Oil</text>

    <line class="rule" x1="92" y1="357" x2="498" y2="357"/>
    <circle class="rule-dot" cx="92" cy="357" r="2.5"/>
    <circle class="rule-dot" cx="498" cy="357" r="2.5"/>

    <text class="product-line product-line--small">
      <textPath href="#arcNarrow" startOffset="25%" text-anchor="middle">Organic</textPath>
    </text>
    <text class="product-line product-line--small">
      <textPath href="#arcNarrow" startOffset="76%" text-anchor="middle">Infusions</textPath>
    </text>

    <rect class="sprig-slot" x="165" y="492" width="75" height="32" rx="14" role="img" aria-label="Sketched herb sprig"/>
    <rect class="sprig-slot" x="350" y="492" width="75" height="32" rx="14" transform="rotate(-12 388 508)" role="img" aria-label="Sketched herb sprig"/>
    <rect class="sketch-slot" x="273" y="378" width="46" height="140" rx="3" role="img" aria-label="Pen sketch of a coastal lighthouse on a rocky shore"/>

    <text class="established" x="295" y="542" text-anchor="middle">Est. 2014</text>
  </g>
</svg>
</body>
</html>
```